Stationery Design Project

see attached logo and business card layout, envelopes, letterhead, proposal, and invoice stationery needs to all flow.

Industry/Entity Type

Business

```html
<!DOCTYPE html>
<html lang="en">
<head>
<meta charset="utf-8">
<title>Summit Paving — Business Card</title>
<link href="https://fonts.googleapis.com/css2?family=Jost:wght@400;500;600&display=swap" rel="stylesheet">
<style>
  :root {
    --backdrop: #c9c9c9;
    --card-dark: #1c1b1b;
    --card-light: #f7f7f7;
    --ink-dark: #2a2a2a;
    --ink-light: #f2f2f2;
    --accent: #e6a417;
  }
  * { margin: 0; padding: 0; box-sizing: border-box; }
  html, body { width: 1200px; height: 900px; overflow: hidden; }
  body {
    background: var(--backdrop);
    font-family: "Jost", sans-serif;
    position: relative;
  }
  .card {
    position: absolute;
    left: 280px;
    width: 640px;
    height: 366px;
    box-shadow: 0 6px 18px rgba(0,0,0,0.18);
  }
  .card--front { top: 64px; background: var(--card-dark); color: var(--ink-light); }
  .card--back  { top: 470px; background: var(--card-light); color: var(--ink-dark); }

  .brand { position: absolute; display: flex; flex-direction: column; }
  .brand__row { display: flex; align-items: center; gap: 12px; }
  .brand__mark { width: 18px; height: 18px; background: var(--accent); }
  .brand__name {
    font-weight: 500;
    font-size: 40px;
    letter-spacing: 1px;
    text-transform: uppercase;
    line-height: 1;
  }
  .brand__tagline {
    font-weight: 500;
    font-size: 15px;
    align-self: flex-end;
    margin-top: 4px;
  }
  .card--front .brand { left: 150px; top: 130px; }
  .card--front .brand__name { color: var(--ink-light); }
  .card--back .brand { left: 48px; top: 96px; }
  .card--back .brand__name { color: var(--ink-dark); font-size: 36px; }
  .card--back .brand__tagline { font-size: 14px; }

  .website {
    position: absolute;
    left: 0; right: 0;
    bottom: 40px;
    text-align: center;
    font-size: 16px;
    letter-spacing: 0.5px;
    color: var(--ink-light);
  }

  .person { position: absolute; right: 44px; top: 72px; text-align: right; }
  .person__name { color: var(--accent); font-weight: 600; font-size: 19px; letter-spacing: 0.5px; }
  .person__title { font-size: 14px; font-weight: 500; }

  .contact {
    position: absolute;
    left: 48px; bottom: 34px;
    font-size: 15px;
    line-height: 1.45;
  }
  .contact__address { font-weight: 500; }
  .contact__line { display: flex; align-items: center; gap: 6px; }
  .contact__icon { width: 15px; height: 15px; flex: none; }
</style>
</head>
<body>
  <section class="card card--front" aria-label="Business card front">
    <div class="brand">
      <div class="brand__row">
        <span class="brand__mark"></span>
        <span class="brand__name">Summit Paving</span>
      </div>
      <span class="brand__tagline">Quality Work Every Time</span>
    </div>
    <p class="website">www.summitpaving.com</p>
  </section>

  <section class="card card--back" aria-label="Business card back">
    <div class="brand">
      <div class="brand__row">
        <span class="brand__mark"></span>
        <span class="brand__name">Summit Paving</span>
      </div>
      <span class="brand__tagline">Quality Work Every Time</span>
    </div>

    <div class="person">
      <p class="person__name">Daniel Carter</p>
      <p class="person__title">Publisher</p>
    </div>

    <div class="contact">
      <p class="contact__address">123, Your Street, Your City, Country, 123.</p>
      <p class="contact__line">
        <svg class="contact__icon" viewBox="0 0 16 16" aria-hidden="true"><path fill="#e6a417" d="M2 6c0-2 2.5-3 6-3s6 1 6 3v1h-3V6H5v1H2zM4 8h8l1 5H3z"/><circle cx="8" cy="10.5" r="1.4" fill="#f7f7f7"/></svg>
        <span>262-555-0148</span>
        <svg class="contact__icon" viewBox="0 0 16 16" aria-hidden="true"><path fill="#e6a417" d="M2 6c0-2 2.5-3 6-3s6 1 6 3v1h-3V6H5v1H2zM4 8h8l1 5H3z"/><circle cx="8" cy="10.5" r="1.4" fill="#f7f7f7"/></svg>
        <span>877-555-0193</span>
      </p>
      <p class="contact__line">
        <svg class="contact__icon" viewBox="0 0 16 16" aria-hidden="true"><rect x="1.5" y="3.5" width="13" height="9" fill="none" stroke="#e6a417" stroke-width="1.5"/><path d="M1.5 3.5 8 9l6.5-5.5" fill="none" stroke="#e6a417" stroke-width="1.5"/></svg>
        <span>carter@summitpaving.com</span>
      </p>
    </div>
  </section>
</body>
</html>
```